依頼詳細
袋のパッケージデザインを依頼させて頂きます。
これまでのパッケージを添付いたしますが、お客様(スーパー)からはこれまでのパッケージと違うデザインを要望されています。デザインの具体的な指示はありません。
購買層は50代~60代の女性
一般NB品と比べてユニットプライスが1.5倍ほど高くなっています。
こだわり米菓ということで、伝統的である程度は高級感が欲しいところです。
品名:藻塩せんべい(書体は自由ですが分かりやすい方がいいです)
コピー:①国産ソラノサチ米100%使用
②淡路島産藻塩使用
③ソラノサチ米のおいしさと旨み際立つ素朴な味わい
以上のコピーを入れてください

表デザインが決定したのちに裏面の展開もお願いいたします。
記載項目
サイズ:200×300 印刷袋 色数4色又は5色まで
希望イメージ
シンプル 複雑
単色 カラフル
暗い 明るい
日常 高級
遊び心 厳粛
未来的 伝統的
女性的 男性的
希望する色
緑系、無彩色系、金色
納品ファイル
• 高解像度JPG (.jpg)
• イラストレーター形式 (.ai)
補足説明
■ 選んだ理由

縦に帯をかけたイメージと緑色のイラストがアクセントとなって高級感を感じる。似たようなデザインがありましたが、色合いと金色を有効的に使用したところで最終的に選びました。

■ 提案者全員のお礼・コメント

この度は多数の素晴らしいデザインをご提案いただきありがとうございました。
選考に大変悩みました。一点に絞らなくてはならないことに心苦しい部分もありました。
貴重なお時間を使い作成していただいたのに申し訳ない気持ちでいっぱいです。
今後もご提案をお願いすることがあると思いますが、
是非、今後ともよろしくお願いいたします。
この度は本当にありがとうございました。

```html
<!DOCTYPE html>
<html lang="ja">
<head>
<meta charset="utf-8">
<title>藻塩せんべい パッケージデザイン案</title>
<link rel="stylesheet" href="https://fonts.googleapis.com/css2?family=Shippori+Mincho+B1:wght@500;700;800&family=Noto+Serif+JP:wght@500;700&display=swap">
<style>
  :root {
    --paper: #ffffff;
    --gold: #c9a862;
    --gold-light: #e6d29c;
    --gold-deep: #a88640;
    --ink: #1d1b19;
    --ink-soft: #2b2825;
    --red: #b8202a;
    --white: #f7f3ea;
    --rice-light: #efe1c2;
    --rice-mid: #d8b77c;
    --rice-dark: #b98a4a;
    --wave-green: #2f6b5a;
    --caption: #333333;
  }
  * { margin: 0; padding: 0; box-sizing: border-box; }
  html, body { width: 878px; height: 1200px; overflow: hidden; background: var(--paper); }
  body { position: relative; font-family: "Shippori Mincho B1", "Noto Serif JP", serif; }

  .sheet-caption {
    position: absolute; left: 12px; top: 10px;
    font-size: 15px; color: var(--caption); letter-spacing: 0.05em;
    font-family: "Noto Serif JP", serif;
  }

  .bag {
    position: absolute; left: 64px; top: 60px; width: 762px; height: 1108px;
    background: var(--rice-light); overflow: hidden;
  }
  .seal { position: absolute; left: 0; width: 100%; height: 60px; }
  .seal--top { top: 0; }
  .seal--bottom { bottom: 0; height: 68px; }

  .product-photo {
    position: absolute; left: 0; top: 60px; width: 100%; height: 980px;
    background:
      radial-gradient(ellipse 60% 30% at 20% 30%, var(--rice-mid), transparent 70%),
      radial-gradient(ellipse 55% 28% at 25% 65%, var(--rice-dark), transparent 70%),
      radial-gradient(ellipse 50% 25% at 85% 50%, var(--rice-mid), transparent 70%),
      linear-gradient(180deg, var(--rice-light), #e4cfa4);
  }

  .label-band {
    position: absolute; left: 186px; top: 62px; width: 520px; height: 978px;
    background: linear-gradient(180deg, var(--ink-soft), var(--ink));
    box-shadow: 0 0 0 1px rgba(201,168,98,0.35);
  }
  .label-band__strip {
    position: absolute; left: 0; top: 0; width: 100%; height: 46px;
    border-bottom: 1px solid var(--gold-deep);
    display: flex; align-items: center; justify-content: center;
    color: var(--gold); font-size: 20px; letter-spacing: 0.55em; font-weight: 700;
  }

  .vertical { position: absolute; writing-mode: vertical-rl; white-space: nowrap; }

  .product-name {
    right: 50px; top: 110px;
    font-size: 108px; font-weight: 800; letter-spacing: 0.04em;
    color: var(--gold-light);
    background: linear-gradient(180deg, var(--gold-light), var(--gold) 55%, var(--gold-deep));
    -webkit-background-clip: text; background-clip: text; -webkit-text-fill-color: transparent;
  }

  .origin-tag {
    position: absolute; right: 200px; top: 250px;
    width: 44px; height: 84px; background: var(--red);
    color: var(--white); font-size: 30px; font-weight: 700;
    writing-mode: vertical-rl; display: flex; align-items: center; justify-content: center;
  }
  .copy-rice { right: 200px; top: 344px; font-size: 30px; font-weight: 700; color: var(--white); letter-spacing: 0.06em; }
  .copy-taste { right: 258px; top: 300px; font-size: 24px; font-weight: 500; color: var(--gold); letter-spacing: 0.08em; }
  .copy-taste-end { right: 300px; top: 330px; font-size: 24px; font-weight: 500; color: var(--gold); letter-spacing: 0.08em; }

  .wave-emblem {
    position: absolute; left: 60px; top: 430px; width: 110px; height: 80px;
    border-radius: 50%;
    background: radial-gradient(circle at 50% 50%, var(--wave-green), #1f4a3e);
  }

  .claim-oil { right: 210px; top: 700px; font-size: 20px; color: var(--white); letter-spacing: 0.12em; }
  .claim-additive { right: 262px; top: 740px; font-size: 20px; color: var(--white); letter-spacing: 0.12em; }
</style>
</head>
<body>
  <p class="sheet-caption">(有) 菓匠そよぎ さま　藻塩せんべいパッケージデザイン案</p>

  <div class="bag">
    <div class="product-photo" role="img" aria-label="積み重ねた藻塩せんべいの写真"></div>

    <svg class="seal seal--top" viewBox="0 0 762 60" preserveAspectRatio="none">
      <defs>
        <linearGradient id="sealGold" x1="0" y1="0" x2="0" y2="1">
          <stop offset="0" stop-color="#e6d29c"/>
          <stop offset="0.5" stop-color="#c9a862"/>
          <stop offset="1" stop-color="#a88640"/>
        </linearGradient>
        <pattern id="crimp" width="6" height="60" patternUnits="userSpaceOnUse">
          <line x1="3" y1="0" x2="3" y2="60" stroke="#a88640" stroke-width="1.2" opacity="0.6"/>
        </pattern>
      </defs>
      <rect width="762" height="60" fill="url(#sealGold)"/>
      <rect width="762" height="60" fill="url(#crimp)"/>
    </svg>

    <div class="label-band">
      <div class="label-band__strip">淡路島産 藻塩使用</div>
      <h1 class="vertical product-name">藻塩せんべい</h1>
      <div class="origin-tag">国産</div>
      <p class="vertical copy-rice">ソラノサチ米100%使用</p>
      <p class="vertical copy-taste">ソラノサチ米のおいしさと旨み際立つ</p>
      <p class="vertical copy-taste-end">素朴な味わい。</p>
      <div class="wave-emblem" role="img" aria-label="緑色の波模様の飾り"></div>
      <p class="vertical claim-oil">キャノーラ油使用</p>
      <p class="vertical claim-additive">化学調味料不使用</p>
    </div>

    <svg class="seal seal--bottom" viewBox="0 0 762 68" preserveAspectRatio="none">
      <rect width="762" height="68" fill="url(#sealGold)"/>
      <rect width="762" height="68" fill="url(#crimp)"/>
    </svg>
  </div>
</body>
</html>
```